new letterhead/envelope/business card design for law firm

please see attached pdf of current letterhead, envelope and business card. I am also attaching my new logo that I would like to be used. basically, I am looking to refresh and simplify my letterhead/stationary and business card, keeping the following in mind:

overall, I am going for the following look:

-simple,
-modern,
-classy,
-professional

Target Market(s)

law firm clients

Industry/Entity Type

Law Firm

Contact Information for Business Card

see attachment

Font styles to use
Sans Serif

Requirements
Must have
• overall, I am going for the following look:
• -simple,
• -modern,
• -classy,
• -professional
Nice to have
• same as above
Should not have
• no serif fonts

```html
<!DOCTYPE html>
<html lang="en">
<head>
<meta charset="utf-8">
<title>Calder Law – Stationery</title>
<link rel="stylesheet" href="https://fonts.googleapis.com/css2?family=Arimo&family=Open+Sans:wght@400;600;700&display=swap">
<style>
  :root {
    --bg: #d4d4d4;
    --paper: #ffffff;
    --navy: #1c2f5a;
    --green: #3c7d3a;
    --ink: #222222;
    --grey: #8a8f98;
    --rule: #c9ccd2;
    --sig: #e6e8ec;
  }
  * { margin: 0; padding: 0; box-sizing: border-box; }
  html, body { width: 1200px; height: 768px; overflow: hidden; }
  body { background: var(--bg); font-family: "Open Sans", sans-serif; position: relative; }

  .sheet { position: absolute; background: var(--paper); box-shadow: 0 2px 8px rgba(0,0,0,.12); }

  .brand { display: flex; align-items: center; gap: 8px; }
  .brand-dot { border-radius: 50%; background: var(--navy); flex: none; }
  .brand-name { font-family: "Open Sans", sans-serif; font-weight: 700; color: var(--navy); letter-spacing: .08em; white-space: nowrap; }

  /* Letterhead */
  .letterhead { left: 620px; top: 30px; width: 540px; height: 700px; padding: 40px 56px; }
  .letterhead .brand { justify-content: flex-end; margin-bottom: 30px; }
  .letterhead .brand-dot { width: 40px; height: 40px; }
  .letterhead .brand-name { font-size: 22px; }
  .letter-body { font-family: "Arimo", sans-serif; font-size: 9.4px; line-height: 1.45; color: var(--ink); }
  .letter-body p { margin-bottom: 12px; }
  .signature { width: 130px; height: 40px; background: var(--sig); margin: 22px 0 0 200px; border-radius: 3px; }
  .letter-footer { position: absolute; left: 56px; right: 56px; bottom: 40px; display: flex; justify-content: center; gap: 22px; font-size: 9px; line-height: 1.45; }
  .footer-divider { width: 1px; background: var(--rule); flex: none; }
  .who strong, .where strong { color: var(--navy); font-weight: 700; display: block; }
  .who span { color: var(--grey); display: block; }
  .where { color: var(--grey); }
  .where b { color: var(--navy); font-weight: 700; }

  /* Business card */
  .card { left: 60px; top: 90px; width: 300px; height: 172px; display: flex; align-items: center; padding: 0 16px; gap: 10px; }
  .card-id { flex: none; }
  .card-id .brand-dot { width: 24px; height: 24px; }
  .card-id .brand-name { font-size: 14px; }
  .card-id .person { margin: 6px 0 0 32px; font-size: 7px; line-height: 1.4; }
  .card-id .person strong { color: var(--navy); display: block; font-weight: 700; }
  .card-id .person span { color: var(--grey); }
  .card .footer-divider { align-self: stretch; margin: 46px 0; }
  .card-contact { font-size: 7px; line-height: 1.5; color: var(--grey); white-space: nowrap; }
  .card-contact b { color: var(--navy); font-weight: 700; }

  /* Envelope */
  .envelope { left: 60px; top: 330px; width: 480px; height: 208px; padding: 22px 26px; }
  .envelope .brand-dot { width: 30px; height: 30px; }
  .envelope .brand-name { font-size: 17px; }
  .return-address { margin-top: 8px; font-size: 9px; line-height: 1.4; font-weight: 700; color: var(--navy); }
</style>
</head>
<body>

<section class="sheet letterhead">
  <div class="brand"><span class="brand-dot"></span><span class="brand-name">CALDER LAW</span></div>
  <div class="letter-body">
    <p>Lorem Ipsum is simply dummy text of the printing and typesetting industry. Lorem Ipsum has been the industry's standard dummy text ever since the 1500s, when an unknown printer took a galley of type and scrambled it to make a type specimen book. It has survived not only five centuries, but also the leap into electronic typesetting, remaining essentially unchanged. It was popularised in the 1960s with the release of Presston transfer sheets containing Lorem Ipsum passages, and more recently with desktop publishing software like Folio LayoutPro including versions of Lorem Ipsum.</p>
    <p>It is a long established fact that a reader will be distracted by the readable content of a page when looking at its layout. The point of using Lorem Ipsum is that it has a more-or-less normal distribution of letters, as opposed to using 'Content here, content here', making it look like readable English. Many desktop publishing packages and web page editors now use Lorem Ipsum as their default model text, and a search for 'lorem ipsum' will uncover many web sites still in their infancy. Various versions have evolved over the years, sometimes by accident, sometimes on purpose (injected humour and the like).</p>
    <p>Contrary to popular belief, Lorem Ipsum is not simply random text. It has roots in a piece of classical Latin literature from 45 BC, making it over 2000 years old. Edwin Harrow, a Latin professor at Linden Hill College in Virginia, looked up one of the more obscure Latin words, consectetur, from a Lorem Ipsum passage, and going through the cites of the word in classical literature, discovered the undoubtable source. Lorem Ipsum comes from sections 1.10.32 and 1.10.33 of an old treatise on ethics, to generate Lorem Ipsum which looks reasonable. The generated Lorem Ipsum is therefore always free from repetition, injected humour.</p>
  </div>
  <div class="signature" role="img" aria-label="Handwritten signature"></div>
  <footer class="letter-footer">
    <div class="who">
      <strong>DANIEL R. CALDER, ESQ.</strong>
      <span>Licensed in NC and FL</span>
      <span>Board Certified in Civil Trial Law</span>
      <span>by the Trial Bar Council</span>
    </div>
    <div class="footer-divider"></div>
    <div class="where">
      <strong>2240 Harlow Lane, Suite 410</strong>
      <strong>Raleigh, NC 27605</strong>
      <div><b>Tel:</b> 919 555 0142</div>
      <div><b>Fax:</b> 919 555 0187</div>
      <div>www.calderlawpa.com</div>
    </div>
  </footer>
</section>

<section class="sheet card">
  <div class="card-id">
    <div class="brand"><span class="brand-dot"></span><span class="brand-name">CALDER LAW</span></div>
    <div class="person"><strong>DANIEL R. CALDER, ESQ.</strong><span>Licensed in NC and FL</span></div>
  </div>
  <div class="footer-divider"></div>
  <div class="card-contact">
    <b>2240 Harlow Lane, Suite 410</b><br>
    <b>Raleigh, NC 27605</b><br>
    <b>Tel:</b> 919 555 0142<br>
    <b>Fax:</b> 919 555 0187<br>
    <b>Cell:</b> 919 555 0163<br>
    www.calderlawpa.com
  </div>
</section>

<section class="sheet envelope">
  <div class="brand"><span class="brand-dot"></span><span class="brand-name">CALDER LAW</span></div>
  <div class="return-address">2240 Harlow Lane, Suite 410<br>Raleigh, NC 27605</div>
</section>

</body>
</html>
```